Dance Card to Provide Contact Info

I'm looking for a double sided business card to provide contact information to perspective dance partners.
One side of the card would have the words: "Yes I would love to Dance" written in an interesting and eye catching way. Below that would be the three categories I'm interested in
>Social >Exhibition >Competition
The other side of the card would include a picture of me with my Name, Phone Number, and Email Address (Dale Pruitt, 210-574-1328, dale@twirlnstep.dance)
My target market is middle aged women interested in Country and Western dancing and West Coast Swing dancing. I am NOT particularly interested in Ballroom style.
Here are a few links to the type of dancing I want to do:
http://www.plvkrn.org/
http://www.prairiefolkstepsociety.com/
http://mesquitevalleytwostep.com/
Dale Pruitt
210-574-1328
dale@twirlnstep.dance

```html
<!DOCTYPE html>
<html lang="en">
<head>
<meta charset="utf-8">
<title>Dale Pruitt – Dance Card</title>
<link rel="stylesheet" href="https://fonts.googleapis.com/css2?family=Montserrat:wght@300;400;600&display=swap">
<style>
  :root {
    --page: #2b2b2d;
    --card-black: #000000;
    --accent-orange: #f7941d;
    --wave-blue: #1b5e8c;
    --text-white: #ffffff;
    --photo-warm: #7a5038;
    --photo-mid: #3a271d;
  }
  * { box-sizing: border-box; margin: 0; padding: 0; }
  html, body {
    width: 1200px; height: 900px; overflow: hidden;
    background: var(--page);
    font-family: "Montserrat", sans-serif;
  }
  .sheet {
    width: 1200px; height: 900px;
    display: flex; flex-direction: column; align-items: center; justify-content: center;
    gap: 60px;
  }
  .card {
    position: relative;
    width: 630px; height: 360px;
    background: var(--card-black);
    border-radius: 24px;
    overflow: hidden;
    box-shadow: 0 12px 28px rgba(0,0,0,0.45);
  }

  /* Front: invitation */
  .card-front { text-align: center; color: var(--text-white); }
  .invite {
    position: absolute; top: 112px; left: 0; right: 0;
  }
  .invite-lead {
    font-weight: 400; font-size: 26px; letter-spacing: 1px; text-transform: uppercase;
  }
  .invite-word {
    font-weight: 600; font-size: 58px; line-height: 1.15;
    color: var(--accent-orange);
  }
  .categories {
    position: absolute; bottom: 42px; left: 0; right: 0;
    display: flex; justify-content: center; align-items: center; gap: 10px;
    font-size: 15px; letter-spacing: 1px; text-transform: uppercase;
  }
  .categories .dot {
    width: 8px; height: 8px; border-radius: 50%; background: var(--accent-orange);
  }

  /* Back: contact */
  .portrait {
    position: absolute; left: 110px; top: 70px; width: 300px; height: 280px;
    background: radial-gradient(ellipse 50% 50% at 50% 45%, var(--photo-warm) 0%, var(--photo-mid) 55%, rgba(0,0,0,0) 100%);
  }
  .wave { position: absolute; inset: 0; width: 100%; height: 100%; }
  .contact {
    position: absolute; right: 42px; top: 140px;
    text-align: right; color: var(--text-white);
  }
  .contact-name {
    font-weight: 400; font-size: 27px; letter-spacing: 1.5px; text-transform: uppercase;
    margin-bottom: 8px;
  }
  .contact-name .first { color: var(--accent-orange); margin-right: 8px; }
  .contact-line {
    display: flex; justify-content: flex-end; align-items: center; gap: 10px;
    font-size: 17px; font-weight: 300; line-height: 1.5;
  }
  .contact-line svg { width: 14px; height: 14px; }
</style>
</head>
<body>
<main class="sheet">

  <section class="card card-front">
    <div class="invite">
      <p class="invite-lead">Yes I would love to</p>
      <p class="invite-word">Dance</p>
    </div>
    <div class="categories">
      <span>Social</span><span class="dot"></span>
      <span>Exhibition</span><span class="dot"></span>
      <span>Competition</span>
    </div>
  </section>

  <section class="card card-back">
    <div class="portrait" role="img" aria-label="Portrait photo of Dale Pruitt smiling in a black shirt"></div>
    <svg class="wave" viewBox="0 0 630 360" preserveAspectRatio="none" aria-hidden="true">
      <path d="M0,280 C170,318 250,210 350,140 C430,88 520,76 630,80 L630,360 L0,360 Z" fill="var(--accent-orange)"/>
      <path d="M0,292 C170,328 252,222 352,152 C432,100 522,89 630,92 L630,360 L0,360 Z" fill="#000"/>
      <path d="M0,296 C170,332 254,226 354,156 C434,104 524,93 630,96 L630,360 L0,360 Z" fill="var(--wave-blue)"/>
    </svg>
    <div class="contact">
      <p class="contact-name"><span class="first">Dale</span>Pruitt</p>
      <p class="contact-line">210-574-1328
        <svg viewBox="0 0 24 24"><path d="M6.6 10.8a15.1 15.1 0 0 0 6.6 6.6l2.2-2.2a1 1 0 0 1 1-.25 11.4 11.4 0 0 0 3.6.57 1 1 0 0 1 1 1V20a1 1 0 0 1-1 1A17 17 0 0 1 3 4a1 1 0 0 1 1-1h3.5a1 1 0 0 1 1 1c0 1.25.2 2.45.57 3.57a1 1 0 0 1-.25 1z" fill="var(--accent-orange)"/></svg>
      </p>
      <p class="contact-line">dale@twirlnstep.dance
        <svg viewBox="0 0 24 24"><rect x="2.5" y="5" width="19" height="14" rx="1.5" fill="none" stroke="var(--accent-orange)" stroke-width="2"/><path d="M3 6l9 7 9-7" fill="none" stroke="var(--accent-orange)" stroke-width="2"/></svg>
      </p>
    </div>
  </section>

</main>
</body>
</html>
```